Medical practice in the United States needs a landing page

Our medical practice, based in Dallas, Texas, is called 'Talwick Headache Clinics.' We perform the Talwick Method on patients to treat chronic, severe head pain.

We currently have a landing page for our Chatterly ads, but we'd like to improve the page's design to increase the lead conversion rate. The landing page contains a form that allows people to register for our free, on-demand informational webinar about the procedure. Either part of the registration form or all of the registration form must be above the fold.

Here is the link to the landing page that needs a more attractive design: https://talwickheadache.example/migraine-treatment-webinars/talwick-treatment-free-patient-webinar/

Once a lead submits the registration form on that page, they are redirected to a different page on the site that contains the webinar video.

Here is a direct link to the page that contains the actual video (note: this is NOT the page for which I am requesting an improved design for this project; I am only including this link so that you can watch the video if you think it will help you create a design for the other page):

https://talwickheadache.example/talwick-headache-clinics-patient-information-webinar/
Updates

Designs look the same

Hello all,

The designs so far have been very impressive! Thank you all for your hard work. Please don't feel compelled to use my exact wording, though, for the description of the webinar. The only requirement is that the form on the page be present and contain the same form fields.

Thanks again!

Target Market(s)

Patients with chronic, severe head pain

Industry/Entity Type

Healthcare

Requirements
Must have
• Either part of the registration form or all of the registration form must be above the fold.
Should not have
• The registration form located completely below the fold.

```html
<!DOCTYPE html>
<html lang="en">
<head>
<meta charset="utf-8">
<title>Talwick Headache Clinics – Registration</title>
<link rel="stylesheet" href="https://fonts.googleapis.com/css2?family=Poppins:wght@400;500;600;700&display=swap">
<style>
  :root {
    --sky: #d3e8f0;
    --lime-wash: #e0f8bd;
    --navy: #02475e;
    --footer: #024960;
    --leaf: #8cc63f;
    --button: #5a9a0f;
    --gold: #f5d27a;
    --white: #ffffff;
    --ink: #1f2d33;
    --placeholder: #6f6f6f;
  }
  * { box-sizing: border-box; margin: 0; padding: 0; }
  html, body { width: 1200px; height: 991px; overflow: hidden; background: var(--white); }
  body { font-family: "Poppins", sans-serif; color: var(--navy); position: relative; }

  .site-header { position: absolute; left: 0; top: 0; width: 1200px; height: 91px; background: var(--sky); }
  .brand { position: absolute; left: 52px; top: 10px; width: 263px; height: 81px; display: flex; align-items: center; gap: 8px; }
  .brand-dot { width: 14px; height: 14px; border-radius: 50%; background: var(--leaf); flex: none; }
  .brand-name { font-size: 19px; font-weight: 500; color: var(--navy); line-height: 1.1; }
  .main-nav { position: absolute; left: 470px; top: 26px; display: flex; gap: 0; }
  .nav-item { display: flex; flex-direction: column; align-items: center; font-size: 11.5px; color: var(--navy); text-decoration: none; }
  .nav-item svg { width: 26px; height: 24px; fill: var(--navy); margin-bottom: 2px; }
  .nav-home { position: absolute; left: 15px; width: 72px; }
  .nav-doctors { position: absolute; left: 96px; width: 130px; }
  .nav-services { position: absolute; left: 224px; width: 84px; }
  .nav-contact { position: absolute; left: 316px; width: 74px; }
  .nav-profile { position: absolute; left: 404px; width: 70px; }

  .hero { position: absolute; left: 0; top: 96px; width: 1200px; height: 280px; background: var(--lime-wash); text-align: center; }
  .hero-title { position: absolute; left: 0; width: 100%; top: 72px; font-size: 52px; font-weight: 500; line-height: 1.2; color: var(--navy); }
  .hero-sub { position: absolute; left: 0; width: 100%; top: 147px; font-size: 23px; font-weight: 400; color: var(--navy); }

  .registration { position: absolute; left: 0; top: 380px; width: 1200px; height: 423px; background: var(--sky); }
  .registration-title { position: absolute; left: 0; width: 100%; top: 15px; text-align: center; font-size: 31px; font-weight: 500; color: var(--navy); }
  .consult-photo { position: absolute; left: 47px; top: 117px; width: 425px; height: 283px; border-radius: 8px; background: linear-gradient(135deg, #cfc6bb 0%, #b39a7c 40%, #e9e6e1 65%, #2a2522 100%); }
  .field-label { position: absolute; left: 613px; font-size: 15.5px; color: var(--ink); }
  .field { position: absolute; left: 763px; width: 337px; background: var(--white); border: none; border-radius: 3px; font-family: "Poppins", sans-serif; font-size: 15.5px; color: var(--placeholder); padding: 5px 6px; }
  .btn-submit { position: absolute; left: 633px; top: 369px; width: 155px; height: 32px; background: var(--button); color: var(--white); border: none; border-radius: 2px; font-family: "Poppins", sans-serif; font-size: 16px; font-weight: 500; }

  .site-footer { position: absolute; left: 0; top: 808px; width: 1200px; height: 183px; background: var(--footer); color: var(--white); }
  .footer-brand { position: absolute; left: 150px; top: 58px; width: 276px; text-align: center; font-size: 22px; font-weight: 400; color: var(--leaf); }
  .footer-col { position: absolute; top: 28px; font-size: 13.5px; line-height: 20.5px; }
  .footer-col h3 { font-size: 14px; font-weight: 700; line-height: 20px; }
  .footer-address { left: 524px; }
  .footer-menu { left: 791px; }
  .contact-line { display: flex; align-items: center; gap: 8px; }
  .contact-line svg { width: 18px; height: 16px; fill: var(--white); }
  .social { position: absolute; left: 1004px; top: 58px; display: flex; gap: 12px; }
  .social span { width: 18px; height: 18px; border-radius: 50%; background: var(--white); display: block; }
  .copyright { position: absolute; left: 0; width: 100%; top: 146px; text-align: center; font-size: 13.5px; font-weight: 700; color: var(--gold); }
</style>
</head>
<body>
  <header class="site-header">
    <div class="brand"><span class="brand-dot"></span><span class="brand-name">Talwick Headache Clinics</span></div>
    <nav class="main-nav">
      <a class="nav-item nav-home" href="#"><svg viewBox="0 0 26 24"><path d="M13 2 1 12h4v10h6v-6h4v6h6V12h4z"/></svg>Home</a>
      <a class="nav-item nav-doctors" href="#"><svg viewBox="0 0 26 24"><circle cx="13" cy="6" r="5"/><path d="M4 23c0-6 4-10 9-10s9 4 9 10z"/></svg>Our Team Doctors</a>
      <a class="nav-item nav-services" href="#"><svg viewBox="0 0 26 24"><path d="M6 2v8a5 5 0 0 0 10 0V2h-2v8a3 3 0 0 1-6 0V2zm4 14v2a5 5 0 0 0 10 0v-3h-2v3a3 3 0 0 1-6 0v-2z"/><circle cx="19" cy="12" r="3"/></svg>Services</a>
      <a class="nav-item nav-contact" href="#"><svg viewBox="0 0 26 24"><path d="M2 4h22v17H2zm4 4v5h5V8zm8 1v2h7V9zm0 4v2h7v-2zM5 17h7v-2H5z"/></svg>Contact</a>
      <a class="nav-item nav-profile" href="#"><svg viewBox="0 0 26 24"><circle cx="13" cy="7" r="6"/><path d="M2 23c0-6 5-9 11-9s11 3 11 9z"/></svg>Profile ▾</a>
    </nav>
  </header>

  <section class="hero">
    <h1 class="hero-title">Talwick Headache Clinics</h1>
    <p class="hero-sub">We perform the Talwick Method on patients to treat chronic, severe head pain</p>
  </section>

  <section class="registration">
    <h2 class="registration-title">Registration form</h2>
    <div class="consult-photo" role="img" aria-label="Photo of a doctor in a white shirt talking with a patient across a desk"></div>
    <form>
      <label class="field-label" style="top:137px">First Name</label>
      <input class="field" style="top:121px;height:32px" placeholder="Your name..">
      <label class="field-label" style="top:194px">Last Name</label>
      <input class="field" style="top:178px;height:32px" placeholder="Your last name..">
      <label class="field-label" style="top:250px">Subject</label>
      <textarea class="field" style="top:234px;height:109px;resize:vertical" placeholder="Write something.."></textarea>
      <button class="btn-submit" type="button">Submit</button>
    </form>
  </section>

  <footer class="site-footer">
    <div class="footer-brand">Talwick Headache Clinics</div>
    <div class="footer-col footer-address">
      <h3>Address</h3>
      <div class="contact-line"><svg viewBox="0 0 18 16"><path d="M3 1h4l1 4-2 1c1 2 3 4 5 5l1-2 4 1v4c-8 0-13-5-13-13z"/></svg>000-000-0000</div>
      <div class="contact-line"><svg viewBox="0 0 18 16"><path d="M1 3h16v2l-8 5-8-5zm0 4 8 5 8-5v7H1z"/></svg>hello@talwickclinics.example</div>
      <div>detail address, DTAIL ADDRESS</div>
    </div>
    <div class="footer-col footer-menu">
      <h3>Menu</h3>
      <div>Home</div>
      <div>Our team doctors Us</div>
      <div>Services</div>
      <div>Contact Us</div>
    </div>
    <div class="social">
      <span aria-label="Proflink"></span>
      <span aria-label="Chatterly"></span>
      <span aria-label="Snapgram"></span>
    </div>
    <p class="copyright">talwick headache clinics | 2023 | All Rights Reserved</p>
  </footer>
</body>
</html>
```